High-End Bifold Brochure for Aesthetics Medspa Business

I need a print-ready, bifold brochure designed for a high-end, luxurious Aesthetics/Medspa practice.

The brochure will showcase the latest IV Therapy content (6 options included in MENU.docx), and exclusive Vitamin B12+ wellness shot content (included in LS PDF). It should also include the business logo and basic office contact options.

The design should be clean, modern, and appealing with a light design. It should flow nicely and compliment the website theme/design. Preferably, having the 6 IV treatments inside bifold, with B12 shot on back/outside page. For easy viewing.

I have attached a few licensed images, if you think they will incorporate into the design nicely. Otherwise, please ignore them. If needed, I can send more.

https://lunavelleskincareclinic.com/
Brand purple: #491c64
Fonts used on site:
Josefin Sans
Montserrat

Size should be 6.5 x 9 using specs on Quillapress's template page (Half Fold design)
https://www.quillapress.com/resources/templates

• Montserrat, Josefin Sans, or similar

• Content included in MENU + B12 shot content on PDF.
Similar feel to the website, High-end, modern, luxurious

```html
<!DOCTYPE html>
<html lang="en">
<head>
<meta charset="utf-8">
<title>Lunavelle Skincare Clinic – Bifold Brochure</title>
<link rel="stylesheet" href="https://fonts.googleapis.com/css2?family=Montserrat:wght@400;500;600;700&family=Oswald:wght@500&display=swap">
<style>
  :root{
    --purple:#6c3695;
    --purple-mid:#7f4ea8;
    --purple-soft:#a27fc4;
    --lavender:#ddd1ec;
    --lavender-pale:#efe9f6;
    --ink:#1f1f1f;
    --rule:#8a8a8a;
    --white:#ffffff;
  }
  *{margin:0;padding:0;box-sizing:border-box}
  html,body{width:900px;height:1200px;overflow:hidden;background:var(--white)}
  body{position:relative;font-family:"Montserrat",sans-serif;color:var(--ink)}
  .sheet{position:absolute;border:1px solid var(--rule);overflow:hidden;background:var(--white)}
  .sheet--outside{left:82px;top:54px;width:738px;height:534px}
  .sheet--inside{left:82px;top:631px;width:738px;height:533px}
  .layer{position:absolute;left:0;top:0}
  .page-label{position:absolute;font-family:"Oswald",sans-serif;font-weight:500;font-size:13px;color:#111;transform:translateX(-50%);letter-spacing:.2px}

  .pill{position:absolute;background:var(--purple);color:var(--white);font-weight:700;text-align:center;border-radius:7px;box-shadow:-4px 4px 0 #b9b3c0}
  .pill--menu{left:77px;top:28px;width:217px;height:25px;font-size:11.5px;line-height:25px}
  .pill--b12{left:439px;top:31px;width:229px;height:33px;font-size:11px;line-height:13.5px;padding-top:3px}
  .pill--benefits{left:492px;top:346px;width:121px;height:22px;font-size:11.5px;line-height:22px}

  /* back panel menu */
  .menu{position:absolute;left:45px;top:75px;width:275px}
  .menu__item{margin-bottom:7px}
  .menu__head{display:flex;align-items:baseline;font-size:9px;font-weight:600;line-height:12.5px;letter-spacing:.1px}
  .menu__leader{flex:1;border-bottom:1px dotted #555;margin:0 2px 3px}
  .menu__price{color:var(--purple);font-weight:700}
  .menu__desc{font-size:9px;line-height:12.5px}
  .site-url{position:absolute;left:0;width:369px;top:502px;text-align:center;color:var(--purple);font-size:9px;font-weight:600}

  /* front panel */
  .brand{position:absolute;left:540px;width:240px;text-align:center;color:var(--white)}
  .brand__mark{position:absolute;left:628px;top:276px;width:40px;height:40px;border:2px solid var(--white);border-radius:50%}
  .brand__name{top:306px;font-size:22px;font-weight:500;line-height:26px}
  .brand__sub{top:333px;font-size:15px;font-weight:500;line-height:18px}
  .brand__rule{position:absolute;left:638px;top:361px;width:41px;height:1px;background:var(--white)}
  .brand__doctor{top:371px;font-size:8.7px;line-height:11px}
  .cta{position:absolute;left:540px;width:240px;text-align:center;color:var(--white)}
  .cta__lead{top:451px;font-size:12px;font-weight:400;opacity:.9}
  .cta__offer{top:466px;font-size:12px;font-weight:500}
  .cta__phone{top:480px;font-size:16.5px;font-weight:700}

  /* inside pages */
  .doctor-name{position:absolute;left:55px;top:100px;color:var(--white);font-weight:700;font-size:11.5px;line-height:13px}
  .doctor-name small{display:block;font-size:8px;font-weight:600}
  .bio{position:absolute;font-size:9.2px;line-height:12.5px}
  .bio p{margin-bottom:6px}
  .bio--one{left:22px;top:200px;width:152px}
  .bio--two{left:194px;top:200px;width:156px}
  .nutrients{position:absolute;left:390px;top:76px;width:335px;list-style:none;font-size:9.3px;line-height:13.6px}
  .nutrients li,.benefits li{position:relative;padding-left:15px}
  .nutrients li::before,.benefits li::before{content:"";position:absolute;left:1px;top:5px;width:3px;height:3px;background:var(--purple);transform:rotate(45deg)}
  .nutrients b{color:var(--purple);font-weight:600}
  .benefits{position:absolute;left:390px;top:379px;width:335px;list-style:none;font-size:9.3px;line-height:13.6px}
</style>
</head>
<body>

<!-- Outside spread: back + front -->
<section class="sheet sheet--outside">
  <svg class="layer" width="738" height="534" viewBox="0 0 738 534">
    <defs>
      <linearGradient id="back-swoosh" x1="0" y1="0" x2="1" y2="1">
        <stop offset="0" stop-color="#ccbde0"/>
        <stop offset="1" stop-color="#ffffff" stop-opacity="0"/>
      </linearGradient>
      <linearGradient id="portrait-tone" x1="0" y1="0" x2="1" y2="0">
        <stop offset="0" stop-color="#f4ded4"/>
        <stop offset="1" stop-color="#e7c7bb"/>
      </linearGradient>
      <linearGradient id="treatment-tone" x1="0" y1="0" x2="1" y2="1">
        <stop offset="0" stop-color="#e9d6cc"/>
        <stop offset="1" stop-color="#9a7f73"/>
      </linearGradient>
    </defs>
    <!-- back swoosh -->
    <path d="M0 136 C140 170 270 260 369 330 L369 534 C300 420 180 300 0 230 Z" fill="url(#back-swoosh)" opacity=".9"/>
    <path d="M200 534 C260 440 320 390 369 350 L369 534 Z" fill="var(--lavender-pale)"/>
    <!-- front: portrait area -->
    <rect x="369" y="0" width="369" height="534" fill="url(#portrait-tone)" role="img" aria-label="Portrait photo of a woman with clear glowing skin touching her face"/>
    <path d="M369 330 C420 360 455 430 470 534 L369 534 Z" fill="var(--purple-mid)"/>
    <path d="M369 300 C430 340 462 420 475 534 L468 534 C455 430 420 350 369 310 Z" fill="var(--purple-soft)"/>
    <!-- front purple sweep -->
    <path d="M545 0 L738 0 L738 534 L552 534 C500 470 480 390 490 320 C505 220 570 160 600 100 C615 60 590 20 545 0 Z" fill="var(--purple)"/>
    <path d="M545 0 C600 25 620 65 600 110 C570 170 510 230 500 320 C490 400 515 480 560 534 L548 534 C500 480 478 400 488 320 C500 220 565 165 592 105 C610 60 585 22 540 0 Z" fill="var(--purple-soft)" opacity=".75"/>
    <path d="M710 0 C730 60 735 150 738 220" stroke="var(--purple-soft)" stroke-width="1" fill="none" opacity=".6"/>
    <!-- treatment photo circle -->
    <circle cx="633" cy="135" r="61" fill="var(--white)"/>
    <circle cx="633" cy="135" r="55" fill="url(#treatment-tone)" role="img" aria-label="Photo of a client receiving a relaxing facial treatment"/>
  </svg>

  <div class="pill pill--menu">The Serene Drop IV Therapy</div>

  <div class="menu">
    <div class="menu__item">
      <div class="menu__head"><span>IMMUNITY BOOSTER</span><span class="menu__leader"></span><span class="menu__price">$150</span></div>
      <p class="menu__desc">Have a cold, flu or just need to give your immunity a boost? Let us mix a powerful punch in our booster bag just for you to prevent or relieve aches and pain</p>
    </div>
    <div class="menu__item">
      <div class="menu__head"><span>REFRESH &amp; HYDRATE</span><span class="menu__leader"></span><span class="menu__price">$100</span></div>
      <p class="menu__desc">Relieve dehydration from the extremes of lifestyle with our balanced electrolyte cocktail targeting jet lag, fatigue, stress and sports related activity to leave you feeling more youthful and refreshed!</p>
    </div>
    <div class="menu__item">
      <div class="menu__head"><span>MIGRAINE BUSTER</span><span class="menu__leader"></span><span class="menu__price">$150</span></div>
      <p class="menu__desc">Eradicate your migraine pain, nausea, vomiting, and light sensitivity with our magic formula</p>
    </div>
    <div class="menu__item">
      <div class="menu__head"><span>WELLNESS INFUSION: Myer’s Cocktail</span><span class="menu__leader"></span><span class="menu__price">$180</span></div>
      <p class="menu__desc">This infusion of vitamins, minerals and electrolytes results in direct access of these nutrients into your cells, enhancing energy, decreasing stress and anxiety in addition to improving memory. Other benefits include relief of asthma, depression, allergies and fibromyalgia pain</p>
    </div>
    <div class="menu__item">
      <div class="menu__head"><span>GLO</span><span class="menu__leader"></span><span class="menu__price">$200</span></div>
      <p class="menu__desc">A Beauty mixture of Glutathione, Biotin and our special formula created to strengthen your hair, nails and skin for that SPECIAL LOOK!</p>
    </div>
    <div class="menu__item">
      <div class="menu__head"><span>THE ULTIMATE WEIGHT LOSS INFUSION</span><span class="menu__leader"></span><span class="menu__price">$200</span></div>
      <p class="menu__desc">Our unique fat burning formula targets fatty deposits resulting in fat expulsion from the body resulting in a more defined and contoured appearance.</p>
    </div>
    <div class="menu__item">
      <div class="menu__head"><span>NAD+ IV: THE FOUNTAIN OF YOUTH</span><span class="menu__leader"></span><span class="menu__price">(+-) $350</span></div>
      <p class="menu__desc">Anti-aging co-enzyme NAD+ in conjunction with Vitamins elevates brain health and beauty, all in one IV treatment!</p>
    </div>
  </div>
  <p class="site-url">www.lunavelleskincareclinic.com</p>

  <span class="brand__mark"></span>
  <p class="brand brand__name">Lunavelle</p>
  <p class="brand brand__sub">Skincare Clinic</p>
  <span class="brand__rule"></span>
  <p class="brand brand__doctor">Daniel Marlow, MD, FACS<br>Master Injector</p>

  <p class="cta cta__lead">Call today for your</p>
  <p class="cta cta__offer">FREE CONSULTATION</p>
  <p class="cta cta__phone">(555) 014-2368</p>
</section>

<span class="page-label" style="left:269px;top:593px">BACK</span>
<span class="page-label" style="left:653px;top:593px">FRONT</span>

<!-- Inside spread -->
<section class="sheet sheet--inside">
  <svg class="layer" width="738" height="533" viewBox="0 0 738 533">
    <defs>
      <linearGradient id="inside-swoosh" x1="0" y1="0" x2="1" y2="0">
        <stop offset="0" stop-color="#ffffff" stop-opacity="0"/>
        <stop offset="1" stop-color="#d9cce8"/>
      </linearGradient>
      <linearGradient id="doctor-tone" x1="0" y1="0" x2="0" y2="1">
        <stop offset="0" stop-color="#b89f8a"/>
        <stop offset="1" stop-color="#e8e6ea"/>
      </linearGradient>
    </defs>
    <path d="M0 410 C200 330 480 270 738 280 L738 533 L0 533 Z" fill="url(#inside-swoosh)" opacity=".55"/>
    <path d="M420 533 C560 480 660 440 738 420 L738 533 Z" fill="var(--lavender)"/>
    <path d="M560 533 C630 500 690 480 738 472 L738 533 Z" fill="var(--purple)"/>
    <path d="M0 0 L503 0 C420 20 360 60 300 110 C230 160 110 185 0 170 Z" fill="var(--purple-mid)"/>
    <path d="M0 0 L430 0 C360 30 320 80 250 120 C180 160 90 175 0 170 Z" fill="var(--purple)"/>
    <path d="M0 40 C40 80 120 85 200 70" stroke="var(--purple-soft)" stroke-width="1" fill="none" opacity=".6"/>
    <circle cx="251" cy="120" r="65" fill="var(--lavender-pale)"/>
    <circle cx="251" cy="120" r="60" fill="var(--white)"/>
    <circle cx="251" cy="120" r="55" fill="url(#doctor-tone)" role="img" aria-label="Portrait photo of the medical director in a white coat"/>
  </svg>

  <p class="doctor-name">Dr. Daniel Marlow<small>M.D., F.A.C.S.</small></p>

  <div class="bio bio--one">
    <p>As founder and Medical Director of Lunavelle Skincare Clinic, <b>Dr. Daniel Marlow, M.D., F.A.C.S.</b> has over 38 experience. Dr, Marlow’s thorough knowledge of anatomy, artistic talent, and attention to detail enable his skillful and precise use of neuromodulators and fillers to minimize lines, wrinkles and volume loss of the face. Dr. Marlow customizes all treatments according to his patient’s individual needs and personally administers all treatments. His patients consistently experience exemplary results with the restoration of a natural and youthful experience.</p>
    <p>Dr. Marlow has been recognize by the Global Council of Medical Practitioners as a Top Physician in Facial</p>
  </div>
  <div class="bio bio--two">
    <p>Rejuvenation and Aesthetics and spotlighted in the Premier Physicians Registry. He is a fellow of the National Guild of Surgeons. He is on the faculty at the Westfield University, College of Medicine, and is a certified Medical Laser Technician and Laser Safety Officer. He was listed in the “Notable Names”, in the state of Arizona.</p>
    <p>Dr. Marlow is wholeheartedly committed to offering the highest quality care in a safe and compassionate environment. He continuously seeks and implements state of the art technology in his practice, he and his highly trained staff regularly complete rigorous continuing education in the most current approaches to patient care and customer services.</p>
  </div>

  <div class="pill pill--b12">Dr. Marlow’s Vitamin B12 Cocktail’s<br>Essential Vitamins and Nutrients</div>

  <ul class="nutrients">
    <li><b>Thiamine -</b> is used by the body to metabolize food for energy and maintain proper health and nerve function</li>
    <li><b>Riboflavin -</b> acts as antioxidant within the body. Riboflavin prevents free radical damage and protects skin and eye health.</li>
    <li><b>Niacinamide -</b> helps maintain a healthy cardiovascular system and metabolism, brain function, healthy skin formation, and aids in the prevention of and management of diabetes.</li>
    <li><b>Pryridoxine -</b> is important for brain development and keeping the nervous and immune systems healthy.</li>
    <li><b>Hydroxocobalamin -</b> helps with DNA synthesis and supports replication. It also helps in the body’s use of fats and carbohydrates for energy, and in the making of new proteins.</li>
    <li><b>Methionine -</b> aids in tissue growth and repair, as well as promoting healthy hair, skin and nails.</li>
    <li><b>Inositol -</b> aids in the metabolic breakdown of fats, and helps reduce blood cholesterol.</li>
    <li><b>L-carnitine -</b> helps convert fatty acids into energy.</li>
    <li><b>Chromium -</b> helps move sugars from the blood system, and turn fats, carbs, and proteins into energy.</li>
  </ul>

  <div class="pill pill--benefits">Overall Benefits</div>

  <ul class="benefits">
    <li>B12 helps aid in red blood cell formation and in DNA synthesis</li>
    <li>Aids in the healthy maintenance of the immune and nervous systems, and other optic nerve</li>
    <li>Helps improve skin tone, and strengthen nails and hair</li>
    <li>Boosts metabolism and energy (which may help reduce craving and encourage weight loss)</li>
    <li>Helps relieve cramping and bloating</li>
    <li>Improves memory (which may protect against Alzheimer’s</li>
    <li>Enhances mood and lessons the effects of depression</li>
  </ul>
</section>

<span class="page-label" style="left:451px;top:1170px">INSIDE PAGES</span>

</body>
</html>
```